2020 Teamwear Price List

Price list of our popular teamwear items that we wholesale to clubs and schools.
looking to create a price list with images, images can be obtained from our website:
www.kelvarrogearhouse.com.au
price list does not have to have lots of details about each product, just a from price. with minimum order etc.
and we can email or post to our clients, so it can be A4 pages/booklet style.
i can also provide images after i choose the design layout we like, so you can just use generic images for now if required.

Target Market(s)

Clubs and Schools

Font styles to use
Sans Serif

Colors

Designer to choose colors to be used in the design.

Requirements
Must have
• Photo or generated image for each product.
Nice to have
• simple format , easy to read , and easy to update from time to time

```html
<!DOCTYPE html>
<html lang="en">
<head>
<meta charset="utf-8">
<title>Kelvarro Gearhouse – Teamwear Price List</title>
<link href="https://fonts.googleapis.com/css2?family=Open+Sans:wght@400;600;700;800&display=swap" rel="stylesheet">
<style>
  :root {
    --black: #0d0d0d;
    --orange: #f04a24;
    --tile: #e1dac3;
    --ink: #111111;
    --muted: #333333;
    --white: #ffffff;
  }
  * { box-sizing: border-box; margin: 0; padding: 0; }
  html, body { width: 927px; height: 1200px; overflow: hidden; background: var(--white); }
  body { font-family: "Open Sans", Arial, sans-serif; color: var(--ink); position: relative; }

  .masthead { position: absolute; left: 0; top: 0; width: 927px; height: 195px; background: var(--black); }
  .brand { position: absolute; left: 72px; top: 72px; display: flex; align-items: center; gap: 14px; }
  .brand-dot { width: 40px; height: 40px; border-radius: 50%; background: var(--orange); }
  .brand-name { color: var(--white); font-weight: 800; font-size: 30px; letter-spacing: 0.5px; line-height: 1.1; }
  .contact { position: absolute; right: 42px; top: 68px; text-align: right; color: var(--white); }
  .contact-label { font-size: 15px; font-weight: 400; }
  .contact-phone { font-size: 24px; font-weight: 700; margin-top: 2px; }
  .contact-email { font-size: 15px; margin-top: 6px; }

  .title-band { position: absolute; left: 0; top: 195px; width: 927px; height: 58px; background: var(--orange);
    display: flex; align-items: center; justify-content: center; }
  .title-band h1 { font-size: 40px; font-weight: 800; color: var(--ink); letter-spacing: 0.5px; }

  .intro { position: absolute; left: 0; top: 261px; width: 927px; text-align: center; font-size: 19px;
    line-height: 24px; color: var(--muted); }

  .products { position: absolute; left: 26px; top: 326px; width: 876px; display: grid;
    grid-template-columns: 288px 288px 288px; grid-auto-rows: 106px; column-gap: 6px; row-gap: 5px; }
  .product { background: var(--tile); position: relative; }
  .product-photo { position: absolute; left: 12px; top: 10px; width: 96px; height: 86px;
    border: 1px solid #8a8a8a; background: radial-gradient(circle at 50% 45%, #ffffff 45%, #cfcfcf 100%); }
  .product-photo.dark { background: radial-gradient(circle at 50% 50%, #3a3d48 30%, #d8d6d2 75%); }
  .product-photo.dark-red { background: radial-gradient(circle at 50% 50%, #1a1a1a 28%, #c84a36 40%, #dedbd6 75%); }
  .product-info { position: absolute; left: 123px; top: 14px; right: 6px; }
  .product-name { font-size: 15px; font-weight: 700; line-height: 18px; }
  .product-note { font-size: 10.5px; line-height: 13px; color: var(--muted); }
  .product-price { font-size: 16px; font-weight: 800; color: var(--orange); margin-top: 2px; }

  .footer-rule { position: absolute; left: 0; top: 1114px; width: 927px; height: 9px; background: var(--orange); }
  .footer { position: absolute; left: 0; top: 1123px; width: 927px; height: 77px; background: var(--black);
    color: var(--white); text-align: center; }
  .footer-main { font-size: 21px; margin-top: 7px; }
  .footer-sub { font-size: 16px; font-weight: 700; margin-top: 1px; }
</style>
</head>
<body>
  <header class="masthead">
    <div class="brand">
      <span class="brand-dot"></span>
      <span class="brand-name">KELVARRO GEARHOUSE</span>
    </div>
    <div class="contact">
      <p class="contact-label">CONTACT US TODAY</p>
      <p class="contact-phone">03 5550 1274</p>
      <p class="contact-email">info@kelvarrogearhouse.com.au</p>
    </div>
  </header>

  <div class="title-band"><h1>TEAMWEAR PRICE LIST</h1></div>

  <p class="intro">Prices shown below exclude GST, Custom Clothing is based on order of 20 + units,<br>smaller order quantities are available on request</p>

  <main class="products">
    <article class="product"><div class="product-photo" role="img" aria-label="White club polo shirt"></div><div class="product-info"><h2 class="product-name">Club Polos</h2><p class="product-note">with 1 logo embroidered</p><p class="product-price">$21.00</p></div></article>
    <article class="product"><div class="product-photo" role="img" aria-label="Club hoodie"></div><div class="product-info"><h2 class="product-name">Club Hoodie</h2><p class="product-note">with 1 logo embroidered</p><p class="product-price">$29.00</p></div></article>
    <article class="product"><div class="product-photo" role="img" aria-label="Sublimated polo shirt"></div><div class="product-info"><h2 class="product-name">Sublimated Polos</h2><p class="product-note">with 1 logo embroidered</p><p class="product-price">$36.00</p></div></article>

    <article class="product"><div class="product-photo" role="img" aria-label="Sublimated tee shirt"></div><div class="product-info"><h2 class="product-name">Sublimated<br>Tee Shirts</h2><p class="product-note">unlimited logos</p><p class="product-price">$35.00</p></div></article>
    <article class="product"><div class="product-photo" role="img" aria-label="Sublimated singlet"></div><div class="product-info"><h2 class="product-name">Sublimated Singlets</h2><p class="product-note">unlimited logos</p><p class="product-price">$31.00</p></div></article>
    <article class="product"><div class="product-photo" role="img" aria-label="Sublimated hoodie"></div><div class="product-info"><h2 class="product-name">Sublimated Hoodies</h2><p class="product-note">unlimited logos</p><p class="product-price">$51.00</p></div></article>

    <article class="product"><div class="product-photo" role="img" aria-label="Walk out shorts"></div><div class="product-info"><h2 class="product-name">Walk Out Shorts</h2><p class="product-note">with 1 logo embroidered</p><p class="product-price">$22.00</p></div></article>
    <article class="product"><div class="product-photo dark" role="img" aria-label="Navy microfibre track pants"></div><div class="product-info"><h2 class="product-name">Microfibre<br>Track Pants</h2><p class="product-note">with 1 logo embroidered</p><p class="product-price">$29.00</p></div></article>
    <article class="product"><div class="product-photo dark-red" role="img" aria-label="Black tapered leg track pant with red stripes"></div><div class="product-info"><h2 class="product-name">Tapered Leg<br>Fleecy Track Pant</h2><p class="product-note">with 1 logo embroidered</p><p class="product-price">$36.00</p></div></article>

    <article class="product"><div class="product-photo" role="img" aria-label="White club polo shirt"></div><div class="product-info"><h2 class="product-name">Club Polos</h2><p class="product-note">with 1 logo embroidered</p><p class="product-price">$21.00</p></div></article>
    <article class="product"><div class="product-photo" role="img" aria-label="Club hoodie"></div><div class="product-info"><h2 class="product-name">Club Hoodie</h2><p class="product-note">with 1 logo embroidered</p><p class="product-price">$29.00</p></div></article>
    <article class="product"><div class="product-photo" role="img" aria-label="Sublimated polo shirt"></div><div class="product-info"><h2 class="product-name">Sublimated Polos</h2><p class="product-note">with 1 logo embroidered</p><p class="product-price">$36.00</p></div></article>

    <article class="product"><div class="product-photo" role="img" aria-label="White club polo shirt"></div><div class="product-info"><h2 class="product-name">Club Polos</h2><p class="product-note">with 1 logo embroidered</p><p class="product-price">$21.00</p></div></article>
    <article class="product"><div class="product-photo" role="img" aria-label="Club hoodie"></div><div class="product-info"><h2 class="product-name">Club Hoodie</h2><p class="product-note">with 1 logo embroidered</p><p class="product-price">$29.00</p></div></article>
    <article class="product"><div class="product-photo" role="img" aria-label="Sublimated polo shirt"></div><div class="product-info"><h2 class="product-name">Sublimated Polos</h2><p class="product-note">with 1 logo embroidered</p><p class="product-price">$36.00</p></div></article>

    <article class="product"><div class="product-photo" role="img" aria-label="White club polo shirt"></div><div class="product-info"><h2 class="product-name">Club Polos</h2><p class="product-note">with 1 logo embroidered</p><p class="product-price">$21.00</p></div></article>
    <article class="product"><div class="product-photo" role="img" aria-label="Club hoodie"></div><div class="product-info"><h2 class="product-name">Club Hoodie</h2><p class="product-note">with 1 logo embroidered</p><p class="product-price">$29.00</p></div></article>
    <article class="product"><div class="product-photo" role="img" aria-label="Sublimated polo shirt"></div><div class="product-info"><h2 class="product-name">Sublimated Polos</h2><p class="product-note">with 1 logo embroidered</p><p class="product-price">$36.00</p></div></article>

    <article class="product"><div class="product-photo" role="img" aria-label="White club polo shirt"></div><div class="product-info"><h2 class="product-name">Club Polos</h2><p class="product-note">with 1 logo embroidered</p><p class="product-price">$21.00</p></div></article>
    <article class="product"><div class="product-photo" role="img" aria-label="Club hoodie"></div><div class="product-info"><h2 class="product-name">Club Hoodie</h2><p class="product-note">with 1 logo embroidered</p><p class="product-price">$29.00</p></div></article>
    <article class="product"><div class="product-photo" role="img" aria-label="Sublimated polo shirt"></div><div class="product-info"><h2 class="product-name">Sublimated Polos</h2><p class="product-note">with 1 logo embroidered</p><p class="product-price">$36.00</p></div></article>
  </main>

  <div class="footer-rule"></div>
  <footer class="footer">
    <p class="footer-main">Please contact us for an official quote – www.kelvarrogearhouse.com.au</p>
    <p class="footer-sub">Ph 03 5550 1274 or email: jordan@kelvarrogearhouse.com.au</p>
  </footer>
</body>
</html>
```